Sheriff Candidate needs a large yard sign

A candidate for Sheriff needs to have a sign to put in front of businesses and houses that advertise her candidacy.

Target Market(s)

Democrats, voters

Industry/Entity Type

Political

Font styles to use
Sans Serif

Colors
34a7d7
3276b5

Requirements
Must have
• Must have her picture
• Must have the words "Elect Dana Holloway" - I'd like the name Dana to be smaller Holloway. "Elect" and "Holloway" should be the focus.
• at the bottom in a box "Paid for by the Committee to Elect Dana Holloway"
Nice to have
• it would be good to have her logo as well.
• blue color for democrats and on a white background
Should not have
• pink color

```html
<!DOCTYPE html>
<html lang="en">
<head>
<meta charset="utf-8">
<title>Elect Dana Holloway – Yard Sign</title>
<link rel="stylesheet" href="https://fonts.googleapis.com/css2?family=Barlow:wght@500;600;700&display=swap">
<style>
  :root {
    --page-bg: #eef1f4;
    --sign-white: #ffffff;
    --sign-haze: #e6f0f6;
    --blue-light: #34a7d7;
    --blue-mid: #3276b5;
    --navy: #123a63;
    --gold: #f2dd7f;
    --gold-dark: #b8912a;
    --photo-dark: #2c3140;
    --photo-warm: #8a6a58;
  }
  * { margin: 0; padding: 0; box-sizing: border-box; }
  html, body { width: 1200px; height: 856px; overflow: hidden; }
  body {
    background: var(--page-bg);
    font-family: "Barlow", Arial, sans-serif;
    position: relative;
  }
  .yard-sign {
    position: absolute;
    left: 40px; top: 204px;
    width: 1120px; height: 448px;
    overflow: hidden;
    background: var(--sign-haze);
    box-shadow: 0 10px 24px rgba(0,0,0,0.18);
  }
  .backdrop-art {
    position: absolute;
    inset: 0;
    background:
      linear-gradient(172deg, rgba(50,118,181,0.85) 0%, rgba(52,167,215,0.6) 22%, rgba(230,240,246,0) 48%),
      linear-gradient(90deg, rgba(52,167,215,0) 60%, rgba(52,167,215,0.55) 78%, rgba(50,118,181,0.8) 100%),
      radial-gradient(ellipse at 50% 55%, var(--sign-white) 0%, var(--sign-haze) 75%);
  }
  .campaign-mark {
    position: absolute;
    left: 81px; top: 171px;
    width: 200px; height: 200px;
    border-radius: 50%;
    background: var(--gold);
    border: 6px solid var(--gold-dark);
    display: flex; align-items: center; justify-content: center;
    text-align: center;
    color: var(--navy);
    font-weight: 700;
    font-size: 24px;
    line-height: 1.1;
    padding: 20px;
    text-transform: uppercase;
  }
  .headline {
    position: absolute;
    left: 308px; top: 186px;
    color: var(--navy);
    line-height: 1;
    text-shadow: 0 0 3px #fff, 0 0 8px #fff;
  }
  .headline-elect {
    display: block;
    font-weight: 500;
    font-size: 72px;
    letter-spacing: 1px;
  }
  .headline-name { display: block; margin-top: 6px; white-space: nowrap; }
  .first-name { font-weight: 500; font-size: 54px; }
  .last-name { font-weight: 700; font-size: 84px; margin-left: 8px; }
  .disclaimer-band {
    position: absolute;
    left: 0; top: 382px;
    width: 778px; height: 36px;
    background: var(--gold);
    color: var(--navy);
    font-weight: 600;
    font-size: 21px;
    line-height: 36px;
    padding-left: 310px;
    white-space: nowrap;
  }
  .candidate-photo {
    position: absolute;
    right: 0; top: 22px;
    width: 330px; height: 426px;
    background: radial-gradient(ellipse at 45% 30%, var(--photo-warm) 0%, #6b5a55 35%, var(--photo-dark) 75%);
  }
</style>
</head>
<body>
  <main class="yard-sign">
    <div class="backdrop-art" role="img" aria-label="Soft blue and white background"></div>

    <div class="campaign-mark">Holloway for Sheriff</div>

    <h1 class="headline">
      <span class="headline-elect">ELECT</span>
      <span class="headline-name"><span class="first-name">Dana</span><span class="last-name">Holloway</span></span>
    </h1>

    <p class="disclaimer-band">Paid for by the Committee to Elect Dana Holloway</p>

    <div class="candidate-photo" role="img" aria-label="Portrait photo of candidate Dana Holloway in a dark blazer"></div>
  </main>
</body>
</html>
```